FixyNestly.com Needs a new Design

We need a card design for a new start up company in the Sacramento Ca area called FixyNestly.com. We offer homeowners three levels of yearly home maintenance memberships that will help them take care of their yearly home maintenance needs even if there on a fixed income.
Our company tag line is ( We Tackle The Chore Lists That Other Crews Skip Past! )
Updates

Information to be put on card. Carl Wenstow Director Phone: 800-537-2916 Fax: 800-537-2916 Address: 4826 Birch Ln Pellford CA 95712

Industry/Entity Type

It Company

```html
<!DOCTYPE html>
<html lang="en">
<head>
<meta charset="utf-8">
<title>FixyNestly.com Business Card</title>
<link rel="stylesheet" href="https://fonts.googleapis.com/css2?family=Ubuntu:wght@400;500;700&display=swap">
<style>
  :root {
    --canvas-bg: #e9e7e3;
    --card-blue-light: #40609a;
    --card-blue: #2f4c86;
    --card-blue-deep: #243d72;
    --accent-orange: #f2733c;
    --text-white: #ffffff;
    --text-soft: #c9d3e8;
    --mark-dark: #1a2340;
  }
  * { box-sizing: border-box; margin: 0; padding: 0; }
  html, body {
    width: 1200px;
    height: 1200px;
    overflow: hidden;
    background: var(--canvas-bg);
    font-family: "Ubuntu", sans-serif;
  }
  .canvas {
    position: relative;
    width: 1200px;
    height: 1200px;
  }
  .card {
    position: absolute;
    left: 150px;
    width: 900px;
    height: 514px;
    border-radius: 4px;
    overflow: hidden;
    box-shadow: 0 6px 18px rgba(0,0,0,0.18);
  }
  .card--front {
    top: 60px;
    background: radial-gradient(ellipse at 75% 10%, var(--card-blue-light) 0%, var(--card-blue) 55%, var(--card-blue-deep) 100%);
  }
  .card--back {
    top: 626px;
    background: radial-gradient(ellipse at 50% 20%, var(--card-blue-light) 0%, var(--card-blue) 55%, var(--card-blue-deep) 100%);
  }

  /* Brand lockup */
  .brand {
    position: absolute;
    display: flex;
    flex-direction: column;
    align-items: center;
    transform: translateX(-50%);
  }
  .brand__row {
    display: flex;
    align-items: center;
    gap: 12px;
  }
  .brand__dot {
    border-radius: 50%;
    background: var(--accent-orange);
  }
  .brand__name {
    color: var(--text-white);
    font-weight: 700;
    letter-spacing: 0.5px;
  }
  .brand__tagline {
    color: var(--text-soft);
    font-weight: 400;
    margin-top: 8px;
    white-space: nowrap;
  }
  .card--front .brand { left: 410px; top: 150px; }
  .card--front .brand__dot { width: 26px; height: 26px; }
  .card--front .brand__name { font-size: 32px; }
  .card--front .brand__tagline { font-size: 11px; }

  .card--back .brand { left: 450px; top: 200px; }
  .card--back .brand__dot { width: 40px; height: 40px; }
  .card--back .brand__name { font-size: 54px; }
  .card--back .brand__tagline { font-size: 15px; }

  /* Contact blocks */
  .contact {
    position: absolute;
    color: var(--text-white);
    font-size: 20px;
    line-height: 1.5;
  }
  .contact__accent {
    color: var(--accent-orange);
    font-weight: 500;
  }
  .contact--person { left: 110px; top: 340px; }
  .contact--place { left: 505px; top: 250px; }
  .contact__line {
    display: flex;
    align-items: center;
    gap: 8px;
  }
  .contact__icon { width: 20px; height: 20px; flex: none; }

  .faint-mark {
    position: absolute;
    right: 60px;
    bottom: -40px;
    width: 260px;
    height: 260px;
    border-radius: 50%;
    background: radial-gradient(circle, rgba(20,32,64,0.35) 0%, rgba(20,32,64,0.08) 70%, rgba(20,32,64,0) 100%);
  }
</style>
</head>
<body>
<main class="canvas">

  <section class="card card--front" aria-label="Card front">
    <div class="brand">
      <div class="brand__row">
        <span class="brand__dot"></span>
        <span class="brand__name">FixyNestly.com</span>
      </div>
      <p class="brand__tagline">We Tackle The Chore Lists That Other Crews Skip Past!</p>
    </div>

    <div class="contact contact--place">
      <p class="contact__accent">Fixynestly.com</p>
      <p>Address:</p>
      <p>4826 Birch Ln Pellford CA 95712</p>
    </div>

    <div class="contact contact--person">
      <p class="contact__accent">Carl Wenstow</p>
      <p>Director</p>
      <p class="contact__line">
        <svg class="contact__icon" viewBox="0 0 20 20" aria-hidden="true">
          <circle cx="10" cy="10" r="8.5" fill="none" stroke="#f2733c" stroke-width="1.8"/>
          <path d="M7 5.5l1.6 2.4-1 1.2c.6 1.3 1.6 2.3 2.9 2.9l1.2-1 2.4 1.6-.9 1.8c-3.5-.3-6.7-3.5-7-7z" fill="#f2733c"/>
        </svg>
        Phone: 800-537-2916
      </p>
      <p class="contact__line">
        <svg class="contact__icon" viewBox="0 0 20 20" aria-hidden="true">
          <circle cx="10" cy="10" r="8.5" fill="none" stroke="#f2733c" stroke-width="1.8"/>
          <path d="M7 5.5l1.6 2.4-1 1.2c.6 1.3 1.6 2.3 2.9 2.9l1.2-1 2.4 1.6-.9 1.8c-3.5-.3-6.7-3.5-7-7z" fill="#f2733c"/>
        </svg>
        Fax: 800-537-2916
      </p>
    </div>
  </section>

  <section class="card card--back" aria-label="Card back">
    <div class="faint-mark" role="img" aria-label="Faint large brand decoration area"></div>
    <div class="brand">
      <div class="brand__row">
        <span class="brand__dot"></span>
        <span class="brand__name">FixyNestly.com</span>
      </div>
      <p class="brand__tagline">We Tackle The Chore Lists That Other Crews Skip Past!</p>
    </div>
  </section>

</main>
</body>
</html>
```